We would like to create the Greating Card for our bussiness partners and friends of our company. Volmira is a group of companies active on the European wholesale energy markets. The company plays an active and diversified role on the European energy market. We tailor our solutions to meet our clients‘ energy needs, using a network that spans Europe while adhering to a strict risk management policy. The Volmira team benefits from our in-depth understanding of the energy sector gained through many years of experience in trading and the expansion of our strategic network.
www.volmira-example.com

Our requirements:
-PF 2016
-topic of the card should be conected with electricity and Christmas
-prefered colors: red, white, black
-our logo is red (you can use it in white color as well)
-we prefer simple design
-not kitsch!

```html
<!DOCTYPE html>
<html lang="en">
<head>
<meta charset="utf-8">
<title>PF 2016 – Volmira</title>
<link rel="stylesheet" href="https://fonts.googleapis.com/css2?family=Calligraffitti&family=Fredericka+the+Great&family=Varela+Round&display=swap">
<style>
  :root {
    --ink-black: #0c0303;
    --deep-maroon: #2a0604;
    --lantern-red: #d8180c;
    --glow-red: #ff3a1e;
    --ember: #7a0e06;
    --snow-white: #ffffff;
  }
  html, body {
    margin: 0;
    padding: 0;
    overflow: hidden;
    background: var(--ink-black);
  }
  .card {
    position: relative;
    width: 1200px;
    height: 799px;
    overflow: hidden;
    background: var(--ink-black);
  }
  .lantern-scene {
    position: absolute;
    inset: 0;
    background:
      radial-gradient(circle at 69% 60%, var(--glow-red) 0%, var(--lantern-red) 18%, var(--ember) 30%, transparent 42%),
      radial-gradient(circle at 29% 44%, var(--lantern-red) 0%, var(--ember) 14%, transparent 24%),
      radial-gradient(ellipse at 40% 80%, rgba(200, 20, 10, 0.45) 0%, transparent 30%),
      linear-gradient(180deg, var(--deep-maroon) 0%, #3a0905 55%, var(--ink-black) 100%);
  }
  .greeting {
    position: absolute;
    top: 22px;
    left: 58px;
    display: flex;
    align-items: baseline;
    gap: 22px;
    color: var(--snow-white);
    margin: 0;
    font-weight: 400;
  }
  .greeting-pf {
    font-family: "Calligraffitti", cursive;
    font-size: 128px;
    line-height: 1;
  }
  .greeting-year {
    font-family: "Fredericka the Great", cursive;
    font-size: 138px;
    line-height: 1;
    letter-spacing: 2px;
    text-shadow: 0 0 6px rgba(255, 255, 255, 0.8), 0 0 14px rgba(255, 255, 255, 0.35);
  }
  .brand-name {
    position: absolute;
    left: 42px;
    bottom: 64px;
    margin: 0;
    font-family: "Varela Round", sans-serif;
    font-size: 96px;
    line-height: 1;
    color: var(--snow-white);
    font-weight: 400;
  }
</style>
</head>
<body>
  <main class="card">
    <div class="lantern-scene" role="img" aria-label="Photograph of two glowing red paper lanterns in a dark room, one sharp in front and one blurred behind"></div>
    <h1 class="greeting">
      <span class="greeting-pf">PF</span>
      <span class="greeting-year">2016</span>
    </h1>
    <p class="brand-name">Volmira</p>
  </main>
</body>
</html>
```